Software Architecture Drawing

I have a software architecture that we would like to pretty up. Our current drawing was done in VISIO, but it just doesn't look professional (and salesy) enough. We would like an illustration that is attractive, makes simple use of colour, and allows us to make little tweaks (wording, etc.). We used icons for certain concepts, but these will have to be redrawn (or purchased). This particular software application is able to receive many data points, store it in a high performance data store, and make it available to various users for analysis or other systems for other purposes

Target Market(s)

Software Architects, IT Professionals

Industry/Entity Type

Software

Font styles to use
Sans Serif

Colors
0355a3
3176b5
85acd3
cedeec
f37022
f68e4e

Requirements
Must have
• Unique (or legal copies) of logos to represent various input sources.

```html
<!DOCTYPE html>
<html lang="en">
<head>
<meta charset="utf-8">
<title>Software Architecture Overview</title>
<link rel="stylesheet" href="https://fonts.googleapis.com/css2?family=Source+Sans+3:wght@400;600&display=swap">
<style>
  :root {
    --ink: #000000;
    --paper: #ffffff;
    --placeholder: #d9d9d9;
    --font: "Source Sans 3", Arial, sans-serif;
  }
  html, body { margin: 0; padding: 0; overflow: hidden; background: var(--paper); }
  .canvas {
    position: relative; width: 1200px; height: 1000px; overflow: hidden;
    background: var(--paper); font-family: var(--font); color: var(--ink);
  }
  .wiring { position: absolute; left: 0; top: 0; }
  .box {
    position: absolute; box-sizing: border-box;
    border: 3px solid var(--ink); border-radius: 8px; background: var(--paper);
    display: flex; align-items: center; justify-content: center; text-align: center;
  }
  .vertical-label {
    transform: rotate(-90deg); white-space: nowrap; line-height: 1.25;
  }
  .ingest { left: 283px; top: 20px; width: 78px; height: 546px; font-size: 30px; }
  .framework { left: 466px; top: 20px; width: 220px; height: 543px; border-radius: 4px; }
  .framework-label {
    position: absolute; left: 4px; top: 20px; width: 86px; height: 470px;
    display: flex; align-items: center; justify-content: center; font-size: 22px;
  }
  .utility { left: 555px; top: 20px; width: 131px; height: 472px; border-radius: 4px; font-size: 22px; align-items: flex-start; }
  .utility .vertical-label { margin-top: 150px; }
  .visual-tools { left: 800px; top: 187px; width: 76px; height: 377px; border-radius: 4px; font-size: 21px; }
  .output { border-radius: 10px; }
  .output-unknown { left: 998px; top: 25px; width: 178px; height: 116px; font-size: 82px; }
  .output-chart { left: 1003px; top: 177px; width: 178px; height: 114px; }
  .output-map { left: 1003px; top: 305px; width: 178px; height: 114px; }
  .output-table { left: 1003px; top: 432px; width: 178px; height: 117px; }
  .map-area { width: 150px; height: 70px; background: var(--placeholder); border-radius: 20px 10px 24px 8px; }
  .web-services { left: 248px; top: 682px; width: 663px; height: 66px; border-radius: 12px; font-size: 44px; }
  .consumer { top: 878px; width: 222px; height: 103px; border-radius: 10px; font-size: 22px; line-height: 1.4; }
  .consumer-presentment { left: 186px; }
  .consumer-conservation { left: 455px; }
  .consumer-clients { left: 717px; }
  .source-label { font-family: var(--font); font-size: 14px; fill: var(--ink); }
  .source-icon { fill: var(--placeholder); }
</style>
</head>
<body>
<main class="canvas">
  <svg class="wiring" width="1200" height="1000" viewBox="0 0 1200 1000">
    <!-- data source stack -->
    <g class="source-stack" fill="var(--paper)" stroke="var(--ink)" stroke-width="2">
      <path d="M33,30 L33,548 Q99,568 165,548 L165,30"/>
      <ellipse cx="99" cy="30" rx="66" ry="13"/>
      <path d="M33,95 Q99,113 165,95" fill="none"/>
      <path d="M33,160 Q99,178 165,160" fill="none"/>
      <path d="M33,238 Q99,256 165,238" fill="none"/>
      <path d="M33,303 Q99,321 165,303" fill="none"/>
      <path d="M33,378 Q99,396 165,378" fill="none"/>
      <path d="M33,443 Q99,461 165,443" fill="none"/>
      <path d="M33,503 Q99,521 165,503" fill="none"/>
    </g>
    <text class="source-label" x="62" y="40" font-size="12">Data Sources</text>
    <rect class="source-icon" x="38" y="55" width="36" height="36" role="img" aria-label="Special source icon"/>
    <text class="source-label" x="92" y="92" font-size="17" transform="rotate(-8 92 92)">Special</text>
    <rect class="source-icon" x="38" y="118" width="34" height="22" role="img" aria-label="Operational source icon"/>
    <text class="source-label" x="72" y="160" transform="rotate(-6 72 160)">Operational</text>
    <rect class="source-icon" x="40" y="178" width="62" height="46" role="img" aria-label="Enterprise source icon"/>
    <text class="source-label" x="74" y="240" transform="rotate(-4 74 240)">Enterprise</text>
    <rect class="source-icon" x="36" y="258" width="36" height="46" role="img" aria-label="Customer source icon"/>
    <text class="source-label" x="84" y="303" transform="rotate(-8 84 303)">Customer</text>
    <rect class="source-icon" x="36" y="325" width="54" height="58" role="img" aria-label="Property source icon"/>
    <text class="source-label" x="95" y="377" transform="rotate(-8 95 377)">Property</text>
    <rect class="source-icon" x="38" y="408" width="38" height="38" role="img" aria-label="Geospatial source icon"/>
    <text class="source-label" x="80" y="440" transform="rotate(-4 80 440)">Geospatial</text>
    <rect x="38" y="466" width="28" height="28" fill="var(--ink)"/>
    <text class="source-label" x="68" y="482" font-size="9">Chirpr</text>
    <text class="source-label" x="80" y="504" font-size="13" transform="rotate(-6 80 504)">Social Media</text>
    <rect class="source-icon" x="36" y="518" width="54" height="30" role="img" aria-label="Weather source icon"/>
    <text class="source-label" x="96" y="548" font-size="13" transform="rotate(-8 96 548)">Weather</text>

    <g fill="var(--paper)" stroke="var(--ink)" stroke-width="3">
      <!-- single right arrows: shaft then head -->
      <g transform="translate(187,58)"><rect x="0" y="-8" width="72" height="16" rx="8"/><path d="M72,-20 A20,20 0 0 1 72,20 Z" fill="var(--ink)" stroke="none"/></g>
      <g transform="translate(187,410)"><rect x="0" y="-8" width="72" height="16" rx="8"/><path d="M72,-20 A20,20 0 0 1 72,20 Z" fill="var(--ink)" stroke="none"/></g>
      <g transform="translate(187,465)"><rect x="0" y="-8" width="72" height="16" rx="8"/><path d="M72,-20 A20,20 0 0 1 72,20 Z" fill="var(--ink)" stroke="none"/></g>
      <g transform="translate(187,525)"><rect x="0" y="-8" width="72" height="16" rx="8"/><path d="M72,-20 A20,20 0 0 1 72,20 Z" fill="var(--ink)" stroke="none"/></g>
      <g transform="translate(787,90)"><rect x="0" y="-8" width="165" height="16" rx="8"/><path d="M165,-20 A20,20 0 0 1 165,20 Z" fill="var(--ink)" stroke="none"/></g>
      <g transform="translate(887,240)"><rect x="0" y="-8" width="62" height="16" rx="8"/><path d="M62,-20 A20,20 0 0 1 62,20 Z" fill="var(--ink)" stroke="none"/></g>
      <g transform="translate(887,362)"><rect x="0" y="-8" width="62" height="16" rx="8"/><path d="M62,-20 A20,20 0 0 1 62,20 Z" fill="var(--ink)" stroke="none"/></g>
      <g transform="translate(893,488)"><rect x="0" y="-8" width="60" height="16" rx="8"/><path d="M60,-20 A20,20 0 0 1 60,20 Z" fill="var(--ink)" stroke="none"/></g>

      <!-- two-way arrows -->
      <g transform="translate(190,125)"><rect x="0" y="-16" width="70" height="14" rx="7" fill="var(--ink)"/><path d="M0,6 A18,18 0 0 1 0,-30 Z" fill="var(--ink)" stroke="none"/><rect x="10" y="2" width="62" height="14" rx="7" fill="var(--ink)"/><path d="M72,-10 A18,18 0 0 1 72,26 Z" fill="var(--ink)" stroke="none"/></g>
      <g transform="translate(190,195)"><rect x="0" y="-16" width="70" height="14" rx="7" fill="var(--ink)"/><path d="M0,6 A18,18 0 0 1 0,-30 Z" fill="var(--ink)" stroke="none"/><rect x="10" y="2" width="62" height="14" rx="7" fill="var(--ink)"/><path d="M72,-10 A18,18 0 0 1 72,26 Z" fill="var(--ink)" stroke="none"/></g>
      <g transform="translate(190,265)"><rect x="0" y="-16" width="70" height="14" rx="7" fill="var(--ink)"/><path d="M0,6 A18,18 0 0 1 0,-30 Z" fill="var(--ink)" stroke="none"/><rect x="10" y="2" width="62" height="14" rx="7" fill="var(--ink)"/><path d="M72,-10 A18,18 0 0 1 72,26 Z" fill="var(--ink)" stroke="none"/></g>
      <g transform="translate(190,335)"><rect x="0" y="-16" width="70" height="14" rx="7" fill="var(--ink)"/><path d="M0,6 A18,18 0 0 1 0,-30 Z" fill="var(--ink)" stroke="none"/><rect x="10" y="2" width="62" height="14" rx="7" fill="var(--ink)"/><path d="M72,-10 A18,18 0 0 1 72,26 Z" fill="var(--ink)" stroke="none"/></g>
      <g transform="translate(378,172)"><rect x="0" y="-16" width="58" height="14" rx="7" fill="var(--ink)"/><path d="M0,6 A18,18 0 0 1 0,-30 Z" fill="var(--ink)" stroke="none"/><rect x="10" y="2" width="50" height="14" rx="7" fill="var(--ink)"/><path d="M60,-10 A18,18 0 0 1 60,26 Z" fill="var(--ink)" stroke="none"/></g>
      <g transform="translate(378,372)"><rect x="0" y="-16" width="58" height="14" rx="7" fill="var(--ink)"/><path d="M0,6 A18,18 0 0 1 0,-30 Z" fill="var(--ink)" stroke="none"/><rect x="10" y="2" width="50" height="14" rx="7" fill="var(--ink)"/><path d="M60,-10 A18,18 0 0 1 60,26 Z" fill="var(--ink)" stroke="none"/></g>
      <g transform="translate(708,375)"><rect x="0" y="-16" width="58" height="14" rx="7" fill="var(--ink)"/><path d="M0,6 A18,18 0 0 1 0,-30 Z" fill="var(--ink)" stroke="none"/><rect x="10" y="2" width="50" height="14" rx="7" fill="var(--ink)"/><path d="M60,-10 A18,18 0 0 1 60,26 Z" fill="var(--ink)" stroke="none"/></g>

      <!-- down arrows -->
      <g transform="translate(600,585)"><rect x="-8" y="0" width="16" height="58" rx="8"/><path d="M-22,58 A22,22 0 0 0 22,58 Z" fill="var(--ink)" stroke="none"/></g>
      <g transform="translate(318,778)"><rect x="-8" y="0" width="16" height="62" rx="8"/><path d="M-22,62 A22,22 0 0 0 22,62 Z" fill="var(--ink)" stroke="none"/></g>
      <g transform="translate(573,778)"><rect x="-8" y="0" width="16" height="62" rx="8"/><path d="M-22,62 A22,22 0 0 0 22,62 Z" fill="var(--ink)" stroke="none"/></g>
      <g transform="translate(830,778)"><rect x="-8" y="0" width="16" height="62" rx="8"/><path d="M-22,62 A22,22 0 0 0 22,62 Z" fill="var(--ink)" stroke="none"/></g>
    </g>
  </svg>

  <div class="box ingest"><span class="vertical-label">Some Text About Here</span></div>

  <div class="box framework">
    <div class="framework-label"><span class="vertical-label">Varden Low-Latency<br>Transaction Execution Framework</span></div>
  </div>
  <div class="box utility"><span class="vertical-label">High-Performance<br>Sensational<br>Utility</span></div>

  <div class="box visual-tools"><span class="vertical-label">All sorts of Visualization Tools</span></div>

  <div class="box output output-unknown">?</div>
  <div class="box output output-chart">
    <svg width="140" height="90" viewBox="0 0 140 90">
      <path d="M4,2 L4,86 L138,86" fill="none" stroke="var(--ink)" stroke-width="3"/>
      <path d="M14,80 L40,52 L60,66 L80,30 L95,58 L130,28" fill="none" stroke="var(--ink)" stroke-width="3"/>
    </svg>
  </div>
  <div class="box output output-map"><div class="map-area" role="img" aria-label="Map with location pins"></div></div>
  <div class="box output output-table">
    <svg width="150" height="88" viewBox="0 0 150 88">
      <rect x="2" y="2" width="146" height="84" fill="none" stroke="var(--ink)" stroke-width="3"/>
      <rect x="2" y="2" width="146" height="10" fill="var(--ink)"/>
      <rect x="2" y="2" width="12" height="84" fill="var(--ink)"/>
      <g stroke="var(--ink)" stroke-width="2">
        <line x1="2" y1="30" x2="148" y2="30"/><line x1="2" y1="48" x2="148" y2="48"/><line x1="2" y1="66" x2="148" y2="66"/>
        <line x1="40" y1="2" x2="40" y2="86"/><line x1="66" y1="2" x2="66" y2="86"/><line x1="92" y1="2" x2="92" y2="86"/><line x1="118" y1="2" x2="118" y2="86"/>
      </g>
    </svg>
  </div>

  <div class="box web-services">Web Services</div>

  <div class="box consumer consumer-presentment">Customer<br>Presentment</div>
  <div class="box consumer consumer-conservation">Conservation<br>Idea</div>
  <div class="box consumer consumer-clients">Custom<br>Clients</div>
</main>
</body>
</html>
```